Medical Billing Business needs a web page designed

We need a web page for a new medical billing business for prospective clients to go to to get information about our company. It needs to show what our company stands for and our billing rates. Our colors are blue, gray and white. I have attached our logo, brochure and mission statement.

Need tabs at top for "about us", "contact us" "specials". On contact page, need a form to fill out that will be automatically emailed to us upon completion. Under specials...Sign a contract by the end of August 2014 and receive one month of billing FREE. ***Receive 25% off the first 4 months of the contract***

```html
<!DOCTYPE html>
<html lang="en">
<head>
<meta charset="utf-8">
<title>Prairieline Medical Billing</title>
<link href="https://fonts.googleapis.com/css2?family=Lato:wght@400;700&family=Oswald:wght@400;500&display=swap" rel="stylesheet">
<style>
:root{
  --teal:#1bb3c8;
  --teal-dark:#1497a8;
  --teal-deep:#0f7f8e;
  --gray:#6e6e6e;
  --gray-dark:#555;
  --text:#555;
  --light:#f1f1f1;
  --white:#fff;
}
*{margin:0;padding:0;box-sizing:border-box}
html,body{width:968px;height:1200px;overflow:hidden;background:var(--white);font-family:'Lato',sans-serif;color:var(--text)}
.page{position:relative;width:968px;height:1200px}
.abs{position:absolute}

.brand{left:106px;top:14px;width:110px;text-align:left}
.brand-mark{width:40px;height:40px;background:var(--teal-deep);margin:0 0 6px 14px}
.brand-name{font-weight:700;font-size:13px;line-height:15px;color:var(--teal-deep)}

.social{display:flex;gap:8px}
.social span{width:24px;height:24px;border-radius:50%;background:var(--teal-dark);display:block}
.top-social{left:741px;top:13px}

.pill{right:106px;height:24px;border-radius:12px 0 0 12px;background:linear-gradient(90deg,#cfcfcf,#f4f4f4 40%,#fff);display:flex;align-items:center;justify-content:flex-end;padding-right:2px;font-weight:700;color:var(--gray-dark);letter-spacing:1.5px;font-size:13.5px}
.pill svg{margin-right:6px}
.pill-phone{top:49px;width:150px}
.pill-mail{top:73px;width:232px}

.nav{left:106px;top:105px;width:756px;height:29px;display:flex;background:var(--teal)}
.nav a{flex:1;text-decoration:none;color:#333;font-size:13px;display:flex;align-items:center;justify-content:center;border-left:1px solid var(--teal-dark)}
.nav a.active{flex:0 0 103px;background:var(--gray);color:var(--white);border:0;position:relative}
.nav a.active::after{content:"";position:absolute;bottom:-1px;left:48px;width:8px;height:4px;border-radius:4px 4px 0 0;background:var(--teal)}

.hero{left:106px;top:134px;width:756px;height:272px;background:linear-gradient(120deg,#9fb2cf 0%,#d9dde3 35%,#eef0f1 60%,#c9ccd0 100%)}
.arrow{top:105px;width:31px;height:37px;background:rgba(90,90,90,.75);display:flex;align-items:center;justify-content:center}
.arrow-l{left:0;border-radius:0 18px 18px 0}
.arrow-r{right:0;border-radius:18px 0 0 18px}
.quote{left:82px;top:182px;width:604px;height:60px;background:rgba(23,160,178,.88);color:var(--white);font-family:'Oswald',sans-serif;font-size:25px;letter-spacing:1.4px;display:flex;align-items:center;justify-content:center}
.quote .q{font-size:26px;position:relative;top:-14px;margin:0 10px}
.hero-rule{left:106px;top:406px;width:756px;height:3px;background:var(--teal)}

.feature-band{left:106px;top:409px;width:756px;height:90px;background:linear-gradient(#d2f3f7,#fff)}
.feature{top:428px;width:188px;text-align:center}
.feature svg{display:block;margin:0 auto}
.feature h3{font-weight:400;font-size:14px;color:var(--teal);margin-top:18px}
.feature p{font-size:10.5px;line-height:16px;margin-top:12px;color:#666}
.feature .more{display:inline-block;margin-top:16px;width:90px;height:24px;line-height:24px;background:var(--teal);color:#3a4a4c;font-size:13px}
.divider{top:506px;height:128px;border-left:1px dotted #bbb}

.services{left:106px;top:680px;width:370px;height:314px;background:var(--light)}
.services-head{height:40px;background:var(--teal);border-bottom:3px solid var(--teal-dark);display:flex;align-items:center;padding-left:10px;gap:8px;font-size:19px;color:#3f6f76}
.services ul{list-style:none;padding:10px 0 0 14px}
.services li{height:33.6px;display:flex;align-items:center;gap:9px;font-size:10.8px;color:#444}

.special{left:491px;top:682px;width:365px;height:312px;background:var(--light);overflow:hidden}
.special svg.bg{position:absolute;left:0;top:0}
.special .lead{position:relative;color:var(--white);font-size:21px;line-height:32px;text-align:center;padding-top:14px}
.special .big{position:relative;text-align:center;font-family:'Oswald',sans-serif;font-weight:500;font-size:48px;color:var(--teal-deep);margin-top:22px;line-height:56px}
.special .sub{position:relative;text-align:center;color:var(--teal);font-size:26px;line-height:40px;margin-top:8px}

.footer{left:106px;top:1010px;width:756px;height:190px;background:linear-gradient(#6b6b6b,#888 60%,#7a7a7a);color:var(--white)}
.info{left:12px;display:flex;gap:10px;font-size:9.5px;line-height:13px}
.info b{display:block;font-weight:400;color:var(--teal);font-size:12px;line-height:14px}
.touch{left:252px;top:14px;font-size:14px}
.field{left:252px;top:38px;width:172px;height:22px;background:var(--white);border:1px solid #ccc;color:#666;font-size:10.5px;letter-spacing:.5px;padding:4px 6px}
.submit{left:251px;top:70px;width:68px;height:22px;background:var(--teal);font-weight:700;font-size:12px;letter-spacing:.5px;display:flex;align-items:center;justify-content:center}
.rule{left:252px;top:108px;width:214px;border-top:1px dashed #999}
.follow{left:252px;top:120px;display:flex;align-items:center;gap:10px;font-size:14px}
.follow .social span{background:#4f6f8a;opacity:.85}
.map{left:488px;top:12px;width:248px;height:138px;background:linear-gradient(135deg,#eef0e8,#e2e6dc);border:2px solid #ddd}
.bottom{left:0;top:160px;width:756px;border-top:1px solid #8a8a8a}
.links{left:10px;top:170px;display:flex;gap:16px;font-size:10px}
.copy{right:20px;top:170px;font-size:10px}
</style>
</head>
<body>
<div class="page">

  <div class="abs brand">
    <div class="brand-mark"></div>
    <div class="brand-name">Prairieline Medical Billing, LLC</div>
  </div>

  <div class="abs social top-social"><span></span><span></span><span></span><span></span></div>

  <div class="abs pill pill-phone">
    <svg width="14" height="16" viewBox="0 0 14 16"><path d="M3 1l3 3-2 2c1 2 3 4 5 5l2-2 3 3-2 3C6 14 1 8 1 3z" fill="#666"/></svg>(555)014-2286
  </div>
  <div class="abs pill pill-mail">
    <svg width="16" height="11" viewBox="0 0 16 11"><rect width="16" height="11" fill="#666"/><path d="M0 0l8 6 8-6" stroke="#ddd" fill="none"/></svg>hello@prairielinebill.com
  </div>

  <nav class="abs nav">
    <a class="active">HOME</a><a>Services</a><a>Solutions</a><a>Testimonials</a><a>Specials</a><a>About us</a><a>Contact us</a>
  </nav>

  <div class="abs hero" role="img" aria-label="Photograph of a stethoscope and pen resting on a medical lab report">
    <div class="abs arrow arrow-l"><svg width="8" height="12"><path d="M7 0v12L0 6z" fill="#fff"/></svg></div>
    <div class="abs arrow arrow-r"><svg width="8" height="12"><path d="M1 0v12l7-6z" fill="#fff"/></svg></div>
    <div class="abs quote"><span class="q">“</span>A Uniquely Personal Approach to Health Care<span class="q">”</span></div>
  </div>
  <div class="abs hero-rule"></div>

  <div class="abs feature-band"></div>

  <div class="abs feature" style="left:106px">
    <svg width="61" height="72" viewBox="0 0 61 72"><path d="M0 6Q30-2 61 6V42Q58 60 30.5 72 3 60 0 42z" fill="#16a7b9"/><rect x="22" y="22" width="17" height="24" rx="2" fill="#555"/><rect x="25" y="25" width="11" height="5" fill="#16a7b9"/><g fill="#16a7b9"><rect x="25" y="33" width="3" height="3"/><rect x="29" y="33" width="3" height="3"/><rect x="33" y="33" width="3" height="3"/><rect x="25" y="38" width="3" height="3"/><rect x="29" y="38" width="3" height="3"/><rect x="33" y="38" width="3" height="3"/></g></svg>
    <h3>Medical Billing and Coding</h3>
    <p>Lorem ipsum dolor si consectetuer adipiscing elit, sed diam sgsv nonummy nibh euismod tinciduntzx dfxfhc.</p>
    <span class="more">Read More</span>
  </div>
  <div class="abs divider" style="left:295px"></div>

  <div class="abs feature" style="left:296px">
    <svg width="61" height="72" viewBox="0 0 61 72"><path d="M0 6Q30-2 61 6V42Q58 60 30.5 72 3 60 0 42z" fill="#16a7b9"/><circle cx="30.5" cy="32" r="11" fill="none" stroke="#555" stroke-width="3"/><circle cx="30.5" cy="32" r="4" fill="#555"/><path d="M27 40h7l-3.5 8z" fill="#555"/></svg>
    <h3>Out of Network Billing</h3>
    <p>Lorem ipsum dolor si consectetuer adipiscing elit, sed diam sgsv nonummy nibh euasismod tinciduntzx dfxfhdf as.</p>
    <span class="more">Read More</span>
  </div>
  <div class="abs divider" style="left:484px"></div>

  <div class="abs feature" style="left:485px">
    <svg width="61" height="72" viewBox="0 0 61 72"><path d="M0 6Q30-2 61 6V42Q58 60 30.5 72 3 60 0 42z" fill="#16a7b9"/><circle cx="30.5" cy="35" r="11" fill="none" stroke="#555" stroke-width="2.5"/><path d="M30.5 28v7h5" stroke="#555" stroke-width="2" fill="none"/><path d="M21 24l4-3M40 24l-4-3" stroke="#555" stroke-width="2.5"/></svg>
    <h3>Appointment Reminder</h3>
    <p>Lorem ipsum dolor si consectetuer adipiscing elit, seasd diam sgsv nonummy nibh asaseuismod tinciduntzx as dsfxfhc.</p>
    <span class="more">Read More</span>
  </div>
  <div class="abs divider" style="left:673px"></div>

  <div class="abs feature" style="left:674px">
    <svg width="61" height="72" viewBox="0 0 61 72"><path d="M0 6Q30-2 61 6V42Q58 60 30.5 72 3 60 0 42z" fill="#16a7b9"/><rect x="20" y="26" width="21" height="18" fill="#555"/><path d="M20 26l4-5h13l4 5" fill="#555"/><path d="M30.5 29v8M26.5 33l4 5 4-5" stroke="#16a7b9" stroke-width="2" fill="none"/></svg>
    <h3>Free EMR Software</h3>
    <p>Lorem ipsum dolor si consectetuer adipiscing elit, sed diam sgsv nonummy nibh euasismod tincdutzx dfxxfhdf as.</p>
    <span class="more">Read More</span>
  </div>

  <section class="abs services">
    <div class="services-head">
      <svg width="20" height="24" viewBox="0 0 20 24"><path d="M1 3Q10 0 19 3V13Q18 19 10 23 2 19 1 13z" fill="none" stroke="#3f6f76" stroke-width="2"/></svg>Our Services
    </div>
    <ul>
      <li><svg width="15" height="15" viewBox="0 0 15 15"><circle cx="7" cy="8" r="6" fill="none" stroke="#444" stroke-width="1.5"/><path d="M4 8l3 3 7-9" stroke="#444" stroke-width="1.8" fill="none"/></svg>Lorem ipsum dolor si consectetuer adipiscing elit, sed diam sgsv.</li>
      <li><svg width="15" height="15" viewBox="0 0 15 15"><circle cx="7" cy="8" r="6" fill="none" stroke="#444" stroke-width="1.5"/><path d="M4 8l3 3 7-9" stroke="#444" stroke-width="1.8" fill="none"/></svg>Ssda Lorem ipsum dolasdor si consectetuer strfd adipiscing.</li>
      <li><svg width="15" height="15" viewBox="0 0 15 15"><circle cx="7" cy="8" r="6" fill="none" stroke="#444" stroke-width="1.5"/><path d="M4 8l3 3 7-9" stroke="#444" stroke-width="1.8" fill="none"/></svg>Lms ipsum dolor si consectetuer adipiscing elit, sed diam end.</li>
      <li><svg width="15" height="15" viewBox="0 0 15 15"><circle cx="7" cy="8" r="6" fill="none" stroke="#444" stroke-width="1.5"/><path d="M4 8l3 3 7-9" stroke="#444" stroke-width="1.8" fill="none"/></svg>Ipsum dolor si consectetuer Lorem adipiscing elit, sed diam sg.</li>
      <li><svg width="15" height="15" viewBox="0 0 15 15"><circle cx="7" cy="8" r="6" fill="none" stroke="#444" stroke-width="1.5"/><path d="M4 8l3 3 7-9" stroke="#444" stroke-width="1.8" fill="none"/></svg>Dolor si consectetuer Lorem ipsum adipiscing elit, sed diam sgsv.</li>
      <li><svg width="15" height="15" viewBox="0 0 15 15"><circle cx="7" cy="8" r="6" fill="none" stroke="#444" stroke-width="1.5"/><path d="M4 8l3 3 7-9" stroke="#444" stroke-width="1.8" fill="none"/></svg>Consectetuer adipiscing elit, sed Lorem ipsum&nbsp; a dolor si diam.</li>
      <li><svg width="15" height="15" viewBox="0 0 15 15"><circle cx="7" cy="8" r="6" fill="none" stroke="#444" stroke-width="1.5"/><path d="M4 8l3 3 7-9" stroke="#444" stroke-width="1.8" fill="none"/></svg>Ctetuer lorem ipsum dolor si conseadipiscing elit, sed diam sg.</li>
      <li><svg width="15" height="15" viewBox="0 0 15 15"><circle cx="7" cy="8" r="6" fill="none" stroke="#444" stroke-width="1.5"/><path d="M4 8l3 3 7-9" stroke="#444" stroke-width="1.8" fill="none"/></svg>Tetuer adipiscing elit, sed lorem ipsum dolor si consec diam.</li>
    </ul>
  </section>

  <section class="abs special">
    <svg class="bg" width="365" height="160" viewBox="0 0 365 160"><path d="M0 0H365V102Q200 175 0 138z" fill="#1bb3c8"/></svg>
    <div class="lead">Sign a contract by the end of<br>August 2014 and receive one<br>month of billing FREE</div>
    <div class="big">25% OFF</div>
    <div class="sub">Receive 25% off the first 4<br>months of the contract</div>
  </section>

  <footer class="abs footer">
    <div class="abs info" style="top:14px">
      <svg width="24" height="24" viewBox="0 0 24 24"><circle cx="12" cy="12" r="10" fill="none" stroke="#1bb3c8" stroke-width="1.5"/><path d="M12 6v6h5" stroke="#1bb3c8" stroke-width="1.5" fill="none"/></svg>
      <div><b>Open everyday</b>from 12a.m. to 2:15p.m.<br>and 6p.m. to midnight</div>
    </div>
    <div class="abs info" style="top:70px">
      <svg width="24" height="22" viewBox="0 0 24 22"><path d="M1 2h14v9H7l-4 3v-3H1z" fill="#1bb3c8"/><path d="M17 6h6v9h-2v3l-4-3h-6v-2h6z" fill="#1bb3c8"/></svg>
      <div style="padding-top:2px"><b style="display:inline">Appointment</b> at (555)014-2286</div>
    </div>
    <div class="abs info" style="top:102px">
      <svg width="24" height="24" viewBox="0 0 24 24"><path d="M12 2a6 6 0 016 6c0 5-6 12-6 12S6 13 6 8a6 6 0 016-6z" fill="#1bb3c8"/><circle cx="12" cy="8" r="2.2" fill="#777"/></svg>
      <div><b>Prairieline Medical Billing</b>418 N Elm Street<br>Alden KS 67000</div>
    </div>

    <div class="abs touch">Stay in Touch</div>
    <div class="abs field">Enter your email here</div>
    <div class="abs submit">SUBMIT</div>
    <div class="abs rule"></div>
    <div class="abs follow">Follow us <div class="social"><span></span><span></span><span></span><span></span></div></div>

    <div class="abs map" role="img" aria-label="Road map of the surrounding area with a pin marking the office location"></div>

    <div class="abs bottom"></div>
    <div class="abs links"><span>Home</span><span>Services</span><span>Solution</span><span>Testimonial</span><span>Specials</span><span>Contact us</span><span>About us</span></div>
    <div class="abs copy">© 2014 PrairielineBill. All Rights Reserved</div>
  </footer>

</div>
</body>
</html>
```